Workplace Safety Consultancy Business needs business card design

We need a business card for a new business providing workplace health and safety consulting called 'Worksure Guard'. We will be providing small to medium sized businesses assistance with OH&S and HR matters to ensure that their employees and the public are safe in the workplace and that they are meeting their legislative requirements. Would like to see the words 'practical workplace safety solutions' on the card. Personal details on the back. It needs to be clean, smart and professional (no fluff). Would like to see a simple logo if possible as well. Have been looking at orange and black, but open to other ideas.
Updates
Thank you to those to have created designs for us so far! We are really impressed with the impact of the black and orange having now seen it. Would be great if any further designs used those colours. Cheers.

Thank you to everyone that submitted a design. Your work is of the highest quality and we had a hard decision deciding. Sorry if we didn't choose your design, but it just came down to the one that stood out to us personally. Cheers.

Target Market(s)
Small-Medium business owners in Queensland, Australia. Age 25-60 male and female. Initially targeting those in the trade type industries
Industry/Entity Type
Health
Look and feel
Each slider illustrates characteristics of the customer's brand and the style your logo design should communicate.

```html
<!DOCTYPE html>
<html lang="en">
<head>
<meta charset="utf-8">
<title>Worksure Guard – Business Card</title>
<link href="https://fonts.googleapis.com/css2?family=Montserrat:ital,wght@0,700;1,300&family=Open+Sans:wght@400;600;700;800&display=swap" rel="stylesheet">
<style>
  :root {
    --page-bg: #dfe5e8;
    --card-black: #231f20;
    --brand-orange: #f26522;
    --logo-grey: #b3b3b3;
    --text-light: #f2f2f2;
    --tagline-grey: #d9d9d9;
    --streak-light: rgba(255,255,255,0.16);
  }
  * { margin: 0; padding: 0; box-sizing: border-box; }
  html, body {
    width: 1200px; height: 900px; overflow: hidden;
    background: var(--page-bg);
  }
  .sheet {
    width: 1200px; height: 900px;
    display: flex; flex-direction: column; align-items: center; justify-content: center;
    gap: 46px;
  }
  .card {
    position: relative;
    width: 660px; height: 377px;
    background: var(--card-black);
    border-radius: 4px;
    box-shadow: 0 6px 18px rgba(0,0,0,0.25);
    overflow: hidden;
  }
  .streak-band {
    position: absolute;
    background: linear-gradient(90deg, transparent 0%, var(--streak-light) 45%, transparent 100%);
  }
  /* front */
  .card-front .wordmark {
    position: absolute; left: 205px; top: 96px;
    display: flex; align-items: center; gap: 18px;
  }
  .card-front .wordmark-square {
    width: 54px; height: 54px; background: var(--brand-orange);
  }
  .card-front .wordmark-name {
    font-family: 'Open Sans', Arial, sans-serif;
    font-weight: 700; font-size: 34px; letter-spacing: 0.5px;
    color: var(--logo-grey); text-transform: uppercase;
  }
  .card-front .streak-band { left: 30px; top: 225px; width: 230px; height: 85px; }
  .card-front .tagline {
    position: absolute; right: 26px; bottom: 26px;
    font-family: 'Montserrat', Arial, sans-serif;
    font-style: italic; font-weight: 300; font-size: 31px;
    color: var(--tagline-grey); letter-spacing: 0.3px;
  }
  /* back */
  .card-back .wordmark {
    position: absolute; left: 40px; top: 40px;
    display: flex; align-items: center; gap: 12px;
  }
  .card-back .wordmark-square {
    width: 30px; height: 30px; background: var(--brand-orange);
  }
  .card-back .wordmark-name {
    font-family: 'Open Sans', Arial, sans-serif;
    font-weight: 800; font-size: 27px; letter-spacing: 0.5px;
    color: var(--text-light); text-transform: uppercase;
  }
  .card-back .streak-band { left: 40px; top: 125px; width: 210px; height: 80px; }
  .contact {
    position: absolute; left: 345px; top: 165px;
    font-family: 'Open Sans', Arial, sans-serif; color: var(--text-light);
  }
  .contact-name {
    font-family: 'Montserrat', Arial, sans-serif;
    font-weight: 700; font-size: 21px; color: var(--brand-orange);
    margin-bottom: 12px; letter-spacing: 0.3px;
  }
  .contact-list { list-style: none; }
  .contact-item {
    display: flex; align-items: center; gap: 12px;
    font-size: 16px; line-height: 25px; font-weight: 600;
  }
  .contact-icon { width: 15px; height: 15px; fill: var(--text-light); flex: none; }
</style>
</head>
<body>
<main class="sheet">
  <section class="card card-front" aria-label="Card front">
    <div class="wordmark">
      <span class="wordmark-square"></span>
      <span class="wordmark-name">Worksure Guard</span>
    </div>
    <div class="streak-band" role="img" aria-label="Soft diagonal light streak decoration"></div>
    <p class="tagline">practical workplace safety solutions</p>
  </section>

  <section class="card card-back" aria-label="Card back">
    <div class="wordmark">
      <span class="wordmark-square"></span>
      <span class="wordmark-name">Worksure Guard</span>
    </div>
    <div class="streak-band" role="img" aria-label="Soft diagonal light streak decoration"></div>
    <div class="contact">
      <p class="contact-name">Daniel Corrigan</p>
      <ul class="contact-list">
        <li class="contact-item">
          <svg class="contact-icon" viewBox="0 0 16 16" aria-hidden="true"><path d="M3.6 1.2l2.3 2.8-1.3 1.7c.9 2 2.4 3.6 4.4 4.6l1.7-1.3 2.9 2.2-1.2 2.6C7 13.4 2.4 8.8 1.2 3z"/></svg>
          <span>0412 555 018</span>
        </li>
        <li class="contact-item">
          <svg class="contact-icon" viewBox="0 0 16 16" aria-hidden="true"><path d="M1 3h14v10H1z M2.2 4.2v.4L8 8.8l5.8-4.2v-.4z" fill-rule="evenodd"/></svg>
          <span>daniel@worksureguard.net.au</span>
        </li>
        <li class="contact-item">
          <svg class="contact-icon" viewBox="0 0 16 16" aria-hidden="true"><path d="M8 1a7 7 0 100 14A7 7 0 008 1zm0 1.3c.8.7 1.5 2 1.8 3.7H6.2C6.5 4.3 7.2 3 8 2.3zM2.4 7.3h2.5v1.4H2.4zm3.8 0h3.6v1.4H6.2zm4.9 0h2.5v1.4h-2.5zM6.2 10h3.6c-.3 1.7-1 3-1.8 3.7-.8-.7-1.5-2-1.8-3.7z"/></svg>
          <span>worksureguard.net.au</span>
        </li>
      </ul>
    </div>
  </section>
</main>
</body>
</html>
```